Vintage Style Soup Package Label

I make dry soup packages. I am looking for a label for my soups that shows Quality, Homemade Goodness. Easy, Delicious. My company is called Uncle Barnaby Pantry, But I want this soup line to be called "Thistle & Rye " All my product has a very Vintage Antique look.
I Love Typography. My 6 cup soups are packaged in a flat black bag.
my website is www.unclebarnabypantry.example. I have 15 different Flavours. Our motto is Simple Suppers, Every Day.
While creating the label if you wanted to use
Please use "Chicken Pot Pie" as your sample please and thanks.

Target Market(s)

I want to sell my soups to upscale Grocery and Specialty stores.

Font styles to use
Serif
Sans Serif
Other font styles liked:
• Castellar

Colors
6c449b
ec1f27
ffc214
9ccb3b
ffffff
f37122

Requirements
Must have
• NOTE: A place for weight needs to be on the label

My labels I print on are Vertical 3.33 x4"
Colours. I do not like Pink or Pastel colours. I prefer Dark or grunge colours.
Nice to have
• NOTE: I live in Canada so my packaging is supposed to have English and French on it. The rule state because I am a small business I do not have to. But if you can figure a way to put in the design that would be fine but not necessary. If you did add it to the design it does not have to be the same size font as the English.
Should not have
• Pastel Colours.

```html
<!DOCTYPE html>
<html lang="en">
<head>
<meta charset="utf-8">
<title>Thistle &amp; Rye by Uncle Barnaby Pantry – Chicken Pot Pie Soup Labels</title>
<link rel="stylesheet" href="https://fonts.googleapis.com/css2?family=Rye&family=Sancreek&family=Oranienbaum&family=Oswald:wght@500&display=swap">
<style>
  :root {
    --canvas: #ffffff;
    --ink: #0b0a09;
    --cream: #efe2c6;
    --paper-light: #e9d2a6;
    --paper-mid: #d8bb8a;
    --paper-dark: #ae8f62;
    --ornament: rgba(60, 40, 20, 0.14);
  }
  * { box-sizing: border-box; margin: 0; padding: 0; }
  html, body { width: 1200px; height: 1200px; overflow: hidden; background: var(--canvas); }
  .canvas { position: relative; width: 1200px; height: 1200px; }

  .label { position: absolute; filter: drop-shadow(4px 5px 4px rgba(0,0,0,0.45)); }
  .label svg.label-art { position: absolute; inset: 0; }
  .label-text { position: absolute; left: 0; width: 100%; text-align: center; white-space: nowrap; }

  .label--banner { left: 227px; top: 152px; width: 407px; height: 210px; }
  .label--front { left: 228px; top: 465px; width: 408px; height: 494px; }

  .company-name {
    font-family: "Rye", serif;
    color: var(--cream);
    font-size: 13px;
    line-height: 16px;
    letter-spacing: 1.5px;
  }
  .line-name {
    font-family: "Rye", serif;
    color: var(--cream);
    font-size: 38px;
    line-height: 44px;
    letter-spacing: 1px;
  }
  .tagline {
    font-family: "Rye", serif;
    color: var(--ink);
    font-size: 17px;
    line-height: 22px;
    letter-spacing: 0.5px;
  }
  .product-name {
    font-family: "Oranienbaum", serif;
    font-weight: 400;
    color: var(--ink);
    font-size: 46px;
    line-height: 44px;
    letter-spacing: 0.5px;
  }
  .product-type {
    font-family: "Sancreek", serif;
    color: var(--ink);
    font-size: 36px;
    line-height: 40px;
    letter-spacing: 2px;
  }
  .descriptor {
    font-family: "Oranienbaum", serif;
    color: var(--ink);
    font-size: 14px;
    line-height: 18px;
    letter-spacing: 0.5px;
  }
  .descriptor span { display: inline-block; border-bottom: 1px solid var(--ink); padding: 0 2px 1px; }
  .prep-time {
    font-family: "Oswald", sans-serif;
    font-weight: 500;
    color: var(--ink);
    font-size: 14px;
    display: flex; align-items: center; justify-content: center; gap: 4px;
  }
  .prep-time .minutes-badge {
    display: inline-flex; align-items: center; justify-content: center;
    width: 22px; height: 22px; border-radius: 50%;
    background: var(--ink); color: var(--cream); font-size: 13px;
  }
  .net-weight {
    font-family: "Oswald", sans-serif;
    font-weight: 500;
    color: var(--cream);
    font-size: 11px;
    line-height: 14px;
    letter-spacing: 2px;
  }
</style>
</head>
<body>
<main class="canvas">

  <!-- Wide banner label -->
  <section class="label label--banner">
    <svg class="label-art" width="407" height="210" viewBox="0 0 407 210">
      <defs>
        <radialGradient id="paperBanner" cx="50%" cy="55%" r="65%">
          <stop offset="0" stop-color="var(--paper-light)"/>
          <stop offset="0.6" stop-color="var(--paper-mid)"/>
          <stop offset="1" stop-color="var(--paper-dark)"/>
        </radialGradient>
      </defs>
      <path d="M0 0 H407 V210 Q203 180 0 210 Z" fill="url(#paperBanner)"/>
      <path d="M16 16 H391 V193 Q203 166 16 193 Z" fill="none" stroke="var(--ink)" stroke-width="2.5"/>
      <path d="M22 22 H385 V187 Q203 161 22 187 Z" fill="none" stroke="var(--ink)" stroke-width="0.8"/>
      <rect x="24" y="22" width="360" height="122" fill="var(--ink)"/>
      <path d="M29 144 H378 V174 Q203 158 29 174 Z" fill="var(--paper-light)" stroke="var(--ink)" stroke-width="0.8"/>
      <line x1="62" y1="45" x2="104" y2="45" stroke="var(--cream)" stroke-width="1.5"/>
      <line x1="303" y1="45" x2="345" y2="45" stroke="var(--cream)" stroke-width="1.5"/>
    </svg>
    <p class="label-text company-name" style="top:37px;">UNCLE BARNABY PANTRY</p>
    <p class="label-text line-name" style="top:70px;">THISTLE &amp; RYE</p>
    <p class="label-text tagline" style="top:148px;">SIMPLE SUPPERS, EVERY DAY</p>
  </section>

  <!-- Vertical front label -->
  <section class="label label--front">
    <svg class="label-art" width="408" height="494" viewBox="0 0 408 494">
      <defs>
        <radialGradient id="paperFront" cx="50%" cy="50%" r="70%">
          <stop offset="0" stop-color="var(--paper-light)"/>
          <stop offset="0.6" stop-color="var(--paper-mid)"/>
          <stop offset="1" stop-color="var(--paper-dark)"/>
        </radialGradient>
      </defs>
      <rect width="408" height="494" fill="url(#paperFront)"/>
      <rect x="16" y="14" width="376" height="465" fill="none" stroke="var(--ink)" stroke-width="2.5"/>
      <rect x="22" y="20" width="364" height="453" fill="none" stroke="var(--ink)" stroke-width="0.8"/>
      <path d="M24 22 H384 V142 Q204 128 24 142 Z" fill="var(--ink)"/>
      <line x1="62" y1="45" x2="104" y2="45" stroke="var(--cream)" stroke-width="1.5"/>
      <line x1="304" y1="45" x2="346" y2="45" stroke="var(--cream)" stroke-width="1.5"/>
      <line x1="58" y1="174" x2="350" y2="174" stroke="var(--ink)" stroke-width="0.8"/>
      <line x1="58" y1="177" x2="350" y2="177" stroke="var(--ink)" stroke-width="0.8"/>
      <line x1="44" y1="279" x2="364" y2="279" stroke="var(--ink)" stroke-width="1.2"/>
      <line x1="60" y1="296" x2="348" y2="296" stroke="var(--ink)" stroke-width="0.8"/>
      <line x1="60" y1="333" x2="348" y2="333" stroke="var(--ink)" stroke-width="0.8"/>
      <line x1="44" y1="347" x2="364" y2="347" stroke="var(--ink)" stroke-width="1.2"/>
      <path d="M169 478 A35 22 0 0 1 239 478 Z" fill="var(--ink)"/>
    </svg>

    <svg class="label-art" width="408" height="494" viewBox="0 0 408 494">
      <rect x="44" y="182" width="68" height="88" rx="20" fill="var(--ornament)" role="img" aria-label="Left scrollwork flourish beside product name"/>
      <rect x="296" y="182" width="68" height="88" rx="20" fill="var(--ornament)" role="img" aria-label="Right scrollwork flourish beside product name"/>
      <rect x="40" y="438" width="40" height="16" rx="8" fill="var(--ornament)" role="img" aria-label="Bottom left corner flourish"/>
      <rect x="328" y="438" width="40" height="16" rx="8" fill="var(--ornament)" role="img" aria-label="Bottom right corner flourish"/>
    </svg>

    <p class="label-text company-name" style="top:37px;">UNCLE BARNABY PANTRY</p>
    <p class="label-text line-name" style="top:70px;">THISTLE &amp; RYE</p>
    <p class="label-text tagline" style="top:145px;">SIMPLE SUPPERS, EVERY DAY</p>
    <h1 class="label-text product-name" style="top:186px;">CHICKEN<br>POT PIE</h1>
    <p class="label-text product-type" style="top:294px;">CUP OF SOUP</p>
    <p class="label-text descriptor" style="top:358px;"><span>SPECIALTY GOURMET</span></p>
    <p class="label-text descriptor" style="top:378px;"><span>TARTE AU POULET</span></p>
    <p class="label-text prep-time" style="top:414px;">READY IN <span class="minutes-badge">3</span> MINUTES</p>
    <p class="label-text net-weight" style="top:461px;">30 G.</p>
  </section>

</main>
</body>
</html>
```